Business Card Design for Cybersecurity Company - Quorvent Systems

We need a business card design for our new cybersecurity company, Quorvent. We’re going for a clean, hi tech look that feels modern, premium, and trustworthy. We want a design that really stands out and makes people say WOW when we hand it over!

Quorvent delivers reliable IT support and managed services for small and mid sized businesses. We help companies stay secure, efficient, and connected through proactive monitoring, cybersecurity services, cloud management, and remote support.

Target Market(s)

Designers should target small and mid sized businesses that need dependable cybersecurity and IT support.

Industry/Entity Type

Cybersecurity, Managed Service Provider, IT services

Contact Information for Business Card

Contact information

Requirements
Must have
• The card should look clean, modern, and tech focused, with the Quorvent logo, clear contact info, and strong readability. It needs to feel premium and professional while still keeping a simple layout that fits a cybersecurity and IT brand.
Nice to have
• Nice to have elements include subtle touches that give the card a modern, tech feel, along with a layout that works well in different background styles.
Should not have
• The card should avoid clutter, loud graphics, or anything that takes attention away from the logo and contact details.

```html
<!DOCTYPE html>
<html lang="en">
<head>
<meta charset="utf-8">
<title>Quorvent Systems – Business Card</title>
<link rel="stylesheet" href="https://fonts.googleapis.com/css2?family=Poppins:wght@300;400;500;600&display=swap">
<style>
  :root{
    --page:#16171a;
    --card:#27282c;
    --card-edge:#1c1d20;
    --texture-light:rgba(255,255,255,.035);
    --texture-dark:rgba(0,0,0,.10);
    --white:#f2f3f5;
    --muted:#b9bcc3;
    --blue:#2f7bff;
    --indigo:#4a5cf8;
    --violet:#7a2cf0;
    --divider:#4a4c52;
  }
  *{box-sizing:border-box;margin:0;padding:0}
  html,body{width:1200px;height:952px;overflow:hidden;background:var(--page);font-family:"Poppins",sans-serif}
  .sheet{position:relative;width:1200px;height:952px}
  .card{position:absolute;left:220px;width:760px;height:434px;background:var(--card);overflow:hidden;
        border-radius:6px;box-shadow:0 10px 30px rgba(0,0,0,.5),0 0 0 1px var(--card-edge)}
  .card--front{top:28px}
  .card--back{top:490px}

  /* faint tech texture area */
  .card__texture{position:absolute;inset:0;pointer-events:none;
    background:
      radial-gradient(ellipse 60% 45% at 18% 22%,var(--texture-light),transparent 70%),
      radial-gradient(ellipse 55% 40% at 85% 80%,var(--texture-light),transparent 70%),
      linear-gradient(135deg,transparent 40%,var(--texture-dark) 100%)}

  /* brand lockup */
  .brand{position:absolute;display:flex;align-items:center;gap:22px;z-index:1}
  .brand__dot{border-radius:50%;background:var(--indigo);flex:none}
  .brand__text{color:var(--white)}
  .brand__name{font-weight:600;line-height:1}
  .brand__sub{font-weight:300;color:var(--muted);line-height:1}

  .card--front .brand{left:150px;top:150px}
  .card--front .brand__dot{width:120px;height:120px}
  .card--front .brand__name{font-size:60px}
  .card--front .brand__sub{font-size:19px;letter-spacing:11px;margin-top:10px}

  .card--back .brand{left:60px;top:150px;gap:14px}
  .card--back .brand__dot{width:56px;height:56px}
  .card--back .brand__name{font-size:34px}
  .card--back .brand__sub{font-size:11px;letter-spacing:6.5px;margin-top:6px}

  .divider{position:absolute;left:370px;top:80px;width:1px;height:274px;z-index:1;
           background:linear-gradient(transparent,var(--divider) 20%,var(--divider) 80%,transparent)}

  .contact{position:absolute;left:410px;top:108px;z-index:1}
  .contact__name{font-size:34px;font-weight:600;line-height:1.1;white-space:nowrap;
     background:linear-gradient(90deg,var(--blue),var(--violet));-webkit-background-clip:text;background-clip:text;color:transparent}
  .contact__role{font-size:12.5px;color:var(--white);margin:6px 0 22px;white-space:nowrap}
  .contact__list{list-style:none}
  .contact__item{display:flex;align-items:center;gap:12px;font-size:15px;color:var(--white);margin-bottom:12px;white-space:nowrap}
  .contact__item svg{width:17px;height:17px;flex:none}
</style>
</head>
<body>
<main class="sheet">
  <section class="card card--front" aria-label="Card front">
    <div class="card__texture" role="img" aria-label="Faint circuit-trace background texture"></div>
    <div class="brand">
      <span class="brand__dot"></span>
      <div class="brand__text">
        <div class="brand__name">Quorvent</div>
        <div class="brand__sub">Systems</div>
      </div>
    </div>
  </section>

  <section class="card card--back" aria-label="Card back">
    <div class="card__texture" role="img" aria-label="Faint circuit-trace background texture"></div>
    <div class="brand">
      <span class="brand__dot"></span>
      <div class="brand__text">
        <div class="brand__name">Quorvent</div>
        <div class="brand__sub">Systems</div>
      </div>
    </div>
    <div class="divider"></div>
    <div class="contact">
      <h1 class="contact__name">Dorian Halvik</h1>
      <p class="contact__role">Owner | CEO | Quorvent Systems</p>
      <ul class="contact__list">
        <li class="contact__item">
          <svg viewBox="0 0 24 24"><path fill="#2f7bff" d="M6.6 10.8a15 15 0 0 0 6.6 6.6l2.2-2.2a1 1 0 0 1 1-.25 11.4 11.4 0 0 0 3.6.57 1 1 0 0 1 1 1V20a1 1 0 0 1-1 1A17 17 0 0 1 3 4a1 1 0 0 1 1-1h3.5a1 1 0 0 1 1 1c0 1.25.2 2.45.57 3.57a1 1 0 0 1-.25 1z"/></svg>
          (855) 640-QUOR
        </li>
        <li class="contact__item">
          <svg viewBox="0 0 24 24"><path fill="#3f68fb" d="M6.6 10.8a15 15 0 0 0 6.6 6.6l2.2-2.2a1 1 0 0 1 1-.25 11.4 11.4 0 0 0 3.6.57 1 1 0 0 1 1 1V20a1 1 0 0 1-1 1A17 17 0 0 1 3 4a1 1 0 0 1 1-1h3.5a1 1 0 0 1 1 1c0 1.25.2 2.45.57 3.57a1 1 0 0 1-.25 1z"/><path d="M15 3a6 6 0 0 1 6 6M15 6.5A2.5 2.5 0 0 1 17.5 9" stroke="#3f68fb" stroke-width="1.8" fill="none"/></svg>
          (813) 555-0192
        </li>
        <li class="contact__item">
          <svg viewBox="0 0 24 24"><rect x="2" y="5" width="20" height="14" rx="1.5" fill="#5a4ef6"/><path d="M3 6l9 7 9-7" stroke="#27282c" stroke-width="1.8" fill="none"/></svg>
          dorian@quorvent.com
        </li>
        <li class="contact__item">
          <svg viewBox="0 0 24 24"><circle cx="12" cy="12" r="9.5" fill="none" stroke="#7a2cf0" stroke-width="2"/><path d="M2.5 12h19M12 2.5c3 3 3 16 0 19M12 2.5c-3 3-3 16 0 19" stroke="#7a2cf0" stroke-width="1.6" fill="none"/></svg>
          quorvent.com
        </li>
      </ul>
    </div>
  </section>
</main>
</body>
</html>
```